business card and statinary comp
BWK LOGO ETC
Professional
MARTIN vale
MANAGER
41 wombery lane east Tallorin 2587
autoshinecrafters@mailhollow.example
autoshinecrafters.example?
rust proofing and prevention complete odour removal systems wash and vacuum thru to a full concourse applications window tinting
appointment time ........... or may also the list of addition comments

```html
<!DOCTYPE html>
<html lang="en">
<head>
<meta charset="utf-8">
<title>BWK Business Card</title>
<link rel="stylesheet" href="https://fonts.googleapis.com/css2?family=Open+Sans:wght@400;600;700&display=swap">
<style>
  :root {
    --stage: #262626;
    --blue-deep: #1f5eb0;
    --blue-light: #4aa0db;
    --swoosh-grey: #b9bcc0;
    --card-white: #ffffff;
    --ink: #5a5d62;
    --ink-soft: #8a8d92;
    --brand-grey: #8e9196;
    --back-dark: #6f7073;
    --back-light: #a4a5a8;
    --back-text: #f2f2f2;
  }
  * { box-sizing: border-box; margin: 0; padding: 0; }
  html, body { width: 1200px; height: 795px; overflow: hidden; }
  body {
    background: var(--stage);
    font-family: "Open Sans", Arial, sans-serif;
    position: relative;
  }
  .card {
    position: absolute;
    top: 242px;
    width: 540px;
    height: 310px;
    border-radius: 18px;
    overflow: hidden;
  }
  .card-front { left: 40px; background: var(--card-white); }
  .card-back {
    left: 620px;
    background: radial-gradient(ellipse at 55% 35%, var(--back-light) 0%, var(--back-dark) 75%);
  }
  .front-band { position: absolute; inset: 0; width: 100%; height: 100%; }
  .holder {
    position: absolute;
    top: 22px;
    right: 30px;
    text-align: right;
    color: var(--card-white);
  }
  .holder-name { font-size: 19px; font-weight: 700; letter-spacing: 0.3px; }
  .holder-role { font-size: 11px; font-weight: 600; letter-spacing: 1px; margin-top: 1px; }
  .contact {
    position: absolute;
    left: 300px;
    top: 128px;
    padding-left: 16px;
    border-left: 1px solid #d9dadc;
    color: var(--ink);
    font-size: 11px;
    line-height: 1.55;
  }
  .contact-address { margin-bottom: 8px; }
  .contact-line { display: flex; align-items: center; gap: 6px; }
  .contact-icon { width: 11px; height: 11px; flex: none; }
  .brand {
    position: absolute;
    left: 40px;
    bottom: 42px;
    display: flex;
    align-items: center;
    gap: 10px;
  }
  .brand-mark { width: 14px; height: 14px; background: var(--blue-deep); }
  .brand-name {
    font-size: 46px;
    font-weight: 700;
    color: var(--brand-grey);
    line-height: 1;
  }
  .back-brand {
    position: absolute;
    top: 86px;
    left: 0;
    right: 0;
    text-align: center;
    font-size: 56px;
    font-weight: 700;
    color: var(--back-text);
  }
  .services {
    position: absolute;
    left: 28px;
    right: 28px;
    bottom: 34px;
    text-align: center;
    color: var(--back-text);
    font-size: 12px;
    line-height: 1.7;
  }
</style>
</head>
<body>
  <section class="card card-front" aria-label="Business card front">
    <svg class="front-band" viewBox="0 0 540 310" preserveAspectRatio="none" aria-hidden="true">
      <defs>
        <linearGradient id="bandBlue" x1="0" y1="1" x2="1" y2="0">
          <stop offset="0" stop-color="var(--blue-light)"/>
          <stop offset="1" stop-color="var(--blue-deep)"/>
        </linearGradient>
      </defs>
      <path d="M0 0 H540 V92 C390 86 200 130 0 270 Z" fill="url(#bandBlue)"/>
      <path d="M0 270 C200 130 390 86 540 92 V104 C390 100 210 150 0 292 Z" fill="var(--swoosh-grey)"/>
    </svg>
    <div class="holder">
      <div class="holder-name">MARTIN vale</div>
      <div class="holder-role">MANAGER</div>
    </div>
    <div class="contact">
      <p class="contact-address">41 wombery lane<br>east Tallorin, 2587</p>
      <p class="contact-line">
        <svg class="contact-icon" viewBox="0 0 12 12" aria-hidden="true"><rect width="12" height="12" rx="2" fill="var(--blue-deep)"/><path d="M3 3.5c0 3 2.5 5.5 5.5 5.5l.8-1.2-1.6-.9-.7.7c-1-.4-1.8-1.2-2.2-2.2l.7-.7-.9-1.6z" fill="#fff"/></svg>
        0265907118
      </p>
      <p class="contact-line">
        <svg class="contact-icon" viewBox="0 0 12 12" aria-hidden="true"><rect width="12" height="12" rx="2" fill="var(--blue-deep)"/><path d="M2.5 3.5h7v5h-7z M2.5 3.5 6 6.3 9.5 3.5" fill="none" stroke="#fff" stroke-width="0.9"/></svg>
        autoshinecrafters@mailhollow.example
      </p>
      <p class="contact-line">
        <svg class="contact-icon" viewBox="0 0 12 12" aria-hidden="true"><circle cx="6" cy="6" r="6" fill="var(--blue-deep)"/><circle cx="6" cy="6" r="3.6" fill="none" stroke="#fff" stroke-width="0.8"/><path d="M2.4 6h7.2M6 2.4v7.2" stroke="#fff" stroke-width="0.7"/></svg>
        autoshinecrafters.example
      </p>
    </div>
    <div class="brand">
      <span class="brand-mark" aria-hidden="true"></span>
      <span class="brand-name">BWK</span>
    </div>
  </section>

  <section class="card card-back" aria-label="Business card back">
    <div class="back-brand">BWK</div>
    <div class="services">
      <p>Rust proofing and prevention • Complete odour removal systems</p>
      <p>Wash and vacuum thru to a full concourse applications • Window tinting</p>
    </div>
  </section>
</body>
</html>
```